Web Design Project

We wish to create a web based logistics exchange for heavy machinery and equipment catering to the mining, oil, gas and infrastructure industries. Customers interested in shipping equipment can post a load on the site and this would then be auctioned off through an online auction to prospective transport providers.Payments would be through direct bank transfer,zenu, plumtender etc.
Both shippers and transport providers gain access via membership.
When a load is posted it would appear on the map indicating its location.Transport providers click on the icon of this map to access information of the pick up and delivery details as well as the load description.
The site would also have links to transport departments and equipment specification sites.
Advertising and merchandising are the other areas of revenue through the site

Target Market(s)

Shippers from Machinery Auction centres and Transport companies

Industry/Entity Type

Catering

Requirements
Must have
• The Logo of the company. The file is attached.

```html
<!DOCTYPE html>
<html lang="en">
<head>
<meta charset="utf-8">
<title>Haulway – Heavy Load Exchange</title>
<link rel="stylesheet" href="https://fonts.googleapis.com/css2?family=Lato:ital,wght@0,300;0,400;0,700;0,900;1,400&display=swap">
<style>
  :root {
    --blue: #1f6fb6;
    --blue-dark: #1a5c9d;
    --orange-top: #ffb01f;
    --orange-bottom: #f27c00;
    --text: #555;
    --nav: #777;
    --grey-band-top: #e4e4e4;
    --grey-band-bottom: #f9f9f9;
    --map-top: #d2d2d2;
    --map-bottom: #b4b4b4;
    --white: #fff;
    --footer: #141414;
    --button-top: #d6d6d6;
    --button-bottom: #9a9a9a;
  }
  * { box-sizing: border-box; margin: 0; padding: 0; }
  html, body { width: 983px; height: 1200px; overflow: hidden; }
  body { font-family: "Lato", sans-serif; background: var(--white); position: relative; color: var(--text); }

  .site-header { position: absolute; left: 0; top: 0; width: 983px; height: 110px; background: var(--white); }
  .brand { position: absolute; left: 106px; top: 42px; display: flex; align-items: center; gap: 12px; }
  .brand-mark { width: 32px; height: 32px; background: var(--blue); }
  .brand-name { font-weight: 900; font-size: 32px; letter-spacing: 2px; color: #2a2a2a; }
  .main-nav a { position: absolute; top: 50px; font-size: 13px; font-weight: 700; color: var(--nav); text-decoration: none; }
  .nav-divider { position: absolute; top: 38px; width: 1px; height: 44px; background: #e2e2e2; }

  .hero { position: absolute; left: 0; top: 110px; width: 983px; height: 104px;
          background: linear-gradient(#3585c5, var(--blue-dark)); border-top: 3px solid #2a78b8; }
  .hero-title { position: absolute; left: 138px; top: 36px; font-size: 27px; font-weight: 300; color: var(--white); }
  .join-button { position: absolute; left: 662px; top: 30px; width: 180px; height: 45px; border-radius: 3px;
                 background: linear-gradient(var(--orange-top), var(--orange-bottom));
                 color: var(--white); font-weight: 900; font-size: 23px; text-align: center; line-height: 45px;
                 box-shadow: 0 2px 3px rgba(0,0,0,.25); }

  .loads-band { position: absolute; left: 0; top: 214px; width: 983px; height: 370px;
                background: linear-gradient(var(--grey-band-top), var(--grey-band-bottom) 85%, var(--white)); }
  .load-item { position: absolute; left: 136px; width: 252px; }
  .load-title { font-size: 14.5px; color: var(--blue); font-weight: 400; }
  .load-desc { font-size: 11.5px; line-height: 15px; margin-top: 6px; }
  .load-meta { display: flex; align-items: center; margin-top: 10px; font-size: 9px; color: var(--blue); font-weight: 700; }
  .load-meta .weight { font-size: 13px; font-weight: 400; margin-right: 10px; }
  .load-meta svg { margin: 0 6px; }
  .small-button { display: inline-block; width: 40px; height: 15px; border-radius: 2px;
                  background: linear-gradient(var(--button-top), var(--button-bottom));
                  color: var(--white); font-size: 9px; font-weight: 700; text-align: center; line-height: 15px; }
  .load-meta .small-button { margin-left: auto; margin-right: 40px; }
  .load-divider { position: absolute; left: 136px; width: 252px; border-top: 1px dotted #666; }
  .view-all { position: absolute; left: 141px; top: 329px; font-size: 11px; font-weight: 700; color: #444; }
  .map-heading { position: absolute; left: 410px; top: 38px; font-size: 17px; color: var(--blue); font-weight: 400; }
  .load-map { position: absolute; left: 466px; top: 70px; width: 326px; height: 268px; border-radius: 6px;
              background: linear-gradient(var(--map-top), var(--map-bottom)); }

  .features { position: absolute; left: 0; top: 584px; width: 983px; }
  .feature { position: absolute; width: 230px; }
  .feature h2 { font-size: 26px; font-weight: 300; color: var(--blue); white-space: nowrap; }
  .feature p { width: 215px; margin: 16px 0 0 6px; font-size: 11px; line-height: 14px; color: var(--text); }
  .feature .small-button { margin: 14px 0 0 4px; width: 50px; height: 18px; line-height: 18px; font-size: 10px; }

  .site-footer { position: absolute; left: 0; top: 1003px; width: 983px; height: 197px; background: var(--footer);
                 background-image: repeating-linear-gradient(45deg, rgba(255,255,255,.03) 0 1px, transparent 1px 3px); }
  .footer-panel { position: absolute; left: 98px; top: 0; width: 786px; height: 34px; background: var(--white); }
  .footer-nav { position: absolute; left: 142px; top: 118px; font-size: 12.5px; font-style: italic; color: var(--white); }
  .footer-brand { position: absolute; left: 690px; top: 85px; display: flex; align-items: center; gap: 10px; }
  .footer-brand .brand-mark { width: 26px; height: 26px; background: #bbb; }
  .footer-brand .brand-name { font-size: 26px; color: #ddd; }
  .legal { position: absolute; right: 135px; top: 133px; font-size: 9px; font-style: italic; color: #ddd; }
</style>
</head>
<body>
  <header class="site-header">
    <div class="brand"><span class="brand-mark"></span><span class="brand-name">HAULWAY</span></div>
    <nav class="main-nav">
      <a href="#" style="left:491px">How it works</a>
      <span class="nav-divider" style="left:586px"></span>
      <a href="#" style="left:606px">Who is using us?</a>
      <span class="nav-divider" style="left:713px"></span>
      <a href="#" style="left:732px">Pricing</a>
      <span class="nav-divider" style="left:787px"></span>
      <a href="#" style="left:806px">Contact</a>
    </nav>
  </header>

  <section class="hero">
    <h1 class="hero-title">Lorem Ipsum Consectetur Adipiscing Elit</h1>
    <a class="join-button">Join us now</a>
  </section>

  <section class="loads-band">
    <article class="load-item" style="top:36px">
      <h3 class="load-title">Lorem Ipsum Consectetur Elit</h3>
      <p class="load-desc">Curabitur lorem justo, euismod quis feugiat eu, malesuada eget erat.</p>
      <div class="load-meta"><span class="weight">20 tons</span>Sydney
        <svg width="14" height="8" viewBox="0 0 14 8"><path d="M0 4h12M9 1l3 3-3 3" stroke="#555" stroke-width="1.3" fill="none"/></svg>
        Alice Springs<span class="small-button">More</span></div>
    </article>
    <div class="load-divider" style="top:124px"></div>
    <article class="load-item" style="top:138px">
      <h3 class="load-title">Lorem Ipsum Consectetur Elit</h3>
      <p class="load-desc">Curabitur lorem justo, euismod quis feugiat eu, malesuada eget erat.</p>
      <div class="load-meta"><span class="weight">20 tons</span>Sydney
        <svg width="14" height="8" viewBox="0 0 14 8"><path d="M0 4h12M9 1l3 3-3 3" stroke="#555" stroke-width="1.3" fill="none"/></svg>
        Alice Springs<span class="small-button">More</span></div>
    </article>
    <div class="load-divider" style="top:220px"></div>
    <article class="load-item" style="top:236px">
      <h3 class="load-title">Lorem Ipsum Consectetur Elit</h3>
      <p class="load-desc">Curabitur lorem justo, euismod quis feugiat eu, malesuada eget erat.</p>
      <div class="load-meta"><span class="weight">20 tons</span>Sydney
        <svg width="14" height="8" viewBox="0 0 14 8"><path d="M0 4h12M9 1l3 3-3 3" stroke="#555" stroke-width="1.3" fill="none"/></svg>
        Alice Springs<span class="small-button">More</span></div>
    </article>
    <div class="load-divider" style="top:316px"></div>
    <a class="view-all">View all &gt;&gt;</a>

    <h2 class="map-heading">Available loads</h2>
    <div class="load-map" role="img" aria-label="Map of the continent showing available load locations with blue markers"></div>
  </section>

  <section class="features">
    <div class="feature" style="left:125px;top:42px"><h2>Lorem Ipsum Elit</h2>
      <p>Lorem ipsum dolor sit amet, consectetur adipiscing elit. Curabitur lorem justo, euismod quis feugiat eu, malesuada eget erat. Class aptent taciti sociosqu ad litora torquent per conubia nostra, per inceptos himenaeos.</p><span class="small-button">More</span></div>
    <div class="feature" style="left:386px;top:42px"><h2>Consectetur Elit</h2>
      <p>Lorem ipsum dolor sit amet, consectetur adipiscing elit. Curabitur lorem justo, euismod quis feugiat eu, malesuada eget erat. Class aptent taciti sociosqu ad litora torquent per conubia nostra, per inceptos himenaeos.</p><span class="small-button">More</span></div>
    <div class="feature" style="left:646px;top:42px"><h2>Adipiscing Lorem</h2>
      <p>Lorem ipsum dolor sit amet, consectetur adipiscing elit. Curabitur lorem justo, euismod quis feugiat eu, malesuada eget erat. Class aptent taciti sociosqu ad litora torquent per conubia nostra, per inceptos himenaeos.</p><span class="small-button">More</span></div>
    <div class="feature" style="left:125px;top:246px"><h2>Consectetur Elit</h2>
      <p>Lorem ipsum dolor sit amet, consectetur adipiscing elit. Curabitur lorem justo, euismod quis feugiat eu, malesuada eget erat. Class aptent taciti sociosqu ad litora torquent per conubia nostra, per inceptos himenaeos.</p><span class="small-button">More</span></div>
    <div class="feature" style="left:386px;top:246px"><h2>Adipiscing Lorem</h2>
      <p>Lorem ipsum dolor sit amet, consectetur adipiscing elit. Curabitur lorem justo, euismod quis feugiat eu, malesuada eget erat. Class aptent taciti sociosqu ad litora torquent per conubia nostra, per inceptos himenaeos.</p><span class="small-button">More</span></div>
    <div class="feature" style="left:646px;top:246px"><h2>Lorem Ipsum Elit</h2>
      <p>Lorem ipsum dolor sit amet, consectetur adipiscing elit. Curabitur lorem justo, euismod quis feugiat eu, malesuada eget erat. Class aptent taciti sociosqu ad litora torquent per conubia nostra, per inceptos himenaeos.</p><span class="small-button">More</span></div>
  </section>

  <footer class="site-footer">
    <div class="footer-panel"></div>
    <nav class="footer-nav">Home | How it works? | Who is using us? | Pricing | Contact</nav>
    <div class="footer-brand"><span class="brand-mark"></span><span class="brand-name">HAULWAY</span></div>
    <div class="legal">Terms of Use | Privacy Policy</div>
  </footer>
</body>
</html>
```